Young Accounting firm needing a captivating business card

We need a business card design that forces the person to look at the card because its either gold foil, plastic, or lettering pop up etc. We already have a logo with a specific gold color and we need to make it pop. We are an accounting firm. I need the words" accounting, payroll, licenses, audits, taxes" somewhere on the business card so as to describe what we do- preferably on the side where the logo is at.

Industry/Entity Type

Accounting

Contact Information for Business Card

Address 48276 9th Ave S Ste 305, Alder Falls, OR 98117
Business Phone (360)418-2096
Fax (360)418-2157
Office Cell Phone (360)586-7319

Font styles to use
Serif

Colors
85abd2

Requirements
Must have
• It should state
• "Accounting" "Taxes" "Audits" "Licenses" "Payroll"
Nice to have
• Matte with gold foil, different textures, With Either a textured ivory background or gray blue slate background
Should not have
• colorful colors

```html
<!DOCTYPE html>
<html lang="en">
<head>
<meta charset="utf-8">
<title>KVLedgerwise – Business Card</title>
<link rel="stylesheet" href="https://fonts.googleapis.com/css2?family=Quicksand:wght@500&family=Arimo:wght@400&display=swap">
<style>
  :root {
    --backdrop: #3a4239;
    --slate-light: #5b6778;
    --slate-mid: #46536a;
    --slate-dark: #2f3d52;
    --gold: #c49a1e;
    --ink-light: #f4f5f7;
  }
  html, body {
    margin: 0;
    width: 1200px;
    height: 1200px;
    overflow: hidden;
    background: var(--backdrop);
  }
  .canvas {
    position: relative;
    width: 1200px;
    height: 1200px;
  }
  .card {
    position: absolute;
    left: 160px;
    width: 880px;
    height: 500px;
    background: linear-gradient(118deg,
      var(--slate-mid) 0%,
      var(--slate-dark) 28%,
      var(--slate-light) 52%,
      var(--slate-dark) 78%,
      var(--slate-mid) 100%);
    box-shadow: 0 10px 30px rgba(0,0,0,0.35);
  }
  .card--contact { top: 70px; }
  .card--front { top: 630px; }

  .brand {
    font-family: "Quicksand", "Arimo", sans-serif;
    font-weight: 500;
    color: var(--gold);
    display: flex;
    align-items: center;
    letter-spacing: 0.5px;
    white-space: nowrap;
  }
  .brand__mark {
    background: var(--gold);
    flex: none;
  }

  /* Contact side */
  .contact-list {
    position: absolute;
    right: 470px;
    top: 150px;
    margin: 0;
    padding: 0;
    list-style: none;
    font-family: "Arimo", sans-serif;
    font-size: 24px;
    line-height: 40px;
    color: var(--ink-light);
    text-align: right;
    white-space: nowrap;
  }
  .contact-list li {
    display: flex;
    justify-content: flex-end;
    align-items: center;
    gap: 14px;
  }
  .contact-list .icon { width: 22px; height: 22px; flex: none; }
  .contact-list .no-icon { width: 22px; flex: none; }
  .divider {
    position: absolute;
    left: 440px;
    top: 140px;
    width: 3px;
    height: 200px;
    background: var(--ink-light);
  }
  .card--contact .brand {
    position: absolute;
    left: 475px;
    top: 205px;
    font-size: 46px;
    gap: 14px;
  }
  .card--contact .brand__mark { width: 40px; height: 40px; }

  /* Front side */
  .card--front .brand {
    position: absolute;
    left: 0;
    right: 0;
    top: 165px;
    justify-content: center;
    font-size: 72px;
    gap: 20px;
  }
  .card--front .brand__mark { width: 60px; height: 60px; }
  .services {
    position: absolute;
    left: 0;
    right: 0;
    top: 300px;
    display: flex;
    justify-content: center;
    gap: 18px;
    margin: 0;
    padding: 0;
    list-style: none;
    font-family: "Arimo", sans-serif;
    font-size: 25px;
    color: var(--ink-light);
  }
  .services li {
    display: flex;
    align-items: center;
    gap: 6px;
  }
  .services li::before {
    content: "";
    width: 13px;
    height: 13px;
    border-radius: 50%;
    background: var(--gold);
  }
</style>
</head>
<body>
<div class="canvas">

  <section class="card card--contact" aria-label="Contact side">
    <ul class="contact-list">
      <li>(360)418-2096
        <svg class="icon" viewBox="0 0 24 24" aria-label="Phone"><circle cx="12" cy="12" r="11" fill="#c49a1e"/><path d="M8 6l2 0 1 3-1.5 1a7 7 0 0 0 4.5 4.5l1-1.5 3 1 0 2a2 2 0 0 1-2 2A10 10 0 0 1 6 8a2 2 0 0 1 2-2z" fill="#2f3d52"/></svg>
      </li>
      <li>(360)418-2157
        <svg class="icon" viewBox="0 0 24 24" aria-label="Fax"><rect x="7" y="2" width="10" height="6" fill="#c49a1e"/><rect x="3" y="8" width="18" height="9" rx="2" fill="#c49a1e"/><rect x="7" y="14" width="10" height="8" fill="#f4f5f7"/></svg>
      </li>
      <li>(360)586-7319
        <svg class="icon" viewBox="0 0 24 24" aria-label="Mobile phone"><circle cx="12" cy="12" r="11" fill="#c49a1e"/><rect x="8.5" y="5" width="7" height="14" rx="1.5" fill="#2f3d52"/></svg>
      </li>
      <li>48276 9th Ave S Ste 305
        <svg class="icon" viewBox="0 0 24 24" aria-label="Location"><path d="M12 2a7 7 0 0 1 7 7c0 5-7 13-7 13S5 14 5 9a7 7 0 0 1 7-7z" fill="#c49a1e"/><circle cx="12" cy="9" r="2.6" fill="#2f3d52"/></svg>
      </li>
      <li>Alder Falls, OR 98117<span class="no-icon"></span></li>
    </ul>
    <div class="divider"></div>
    <div class="brand"><span class="brand__mark"></span>KVLedgerwise</div>
  </section>

  <section class="card card--front" aria-label="Front side">
    <div class="brand"><span class="brand__mark"></span>KVLedgerwise</div>
    <ul class="services">
      <li>Accounting</li>
      <li>Taxes</li>
      <li>Audits</li>
      <li>Licenses</li>
      <li>Payroll</li>
    </ul>
  </section>

</div>
</body>
</html>
```